依頼詳細

1面は車検入庫促進に関する内容で『安心・安全・快適なカーライフを』
早期予約割引、3カ月以上前3,000円、2カ月前2,000円、1カ月前1,000円
お早めのご予約をお待ちしております。車検は満了日の1か月前から受けることができます。の記載をお願いします。車検の信頼を表すのには青系、割引部分は赤やオレンジ系が良いかと思います。

2面目は代替を検討されている方へ、弊社でも新車・中古車販売、現在お乗りのお車の買取をやっていることを知って頂きたいことが目的です。
新車・中古車・買取の3ブロック構成で新車・中古車部分を重視します。

【新車販売】新車販売の枠に通常の新車販売『国産全メーカー全車種取り扱い可能』な点と今流行りの定額カーリースをはじめました。ことを伝えたいです。
新しい車の買い方として「車両」「車検」「税金」「メンテナンス」などのマイカーに関わる出費をコミコミ定額にできるマイカーリースがブームです。
「車両」「車検」「税金」「メンテナンス」などの急な出費がなく毎月定額で資金計画も立てやすくなります。定額な点を重視します。

【中古車販売】お客様のご希望の中古車をご予算に応じて提携各ディーラーや全国の中古車オークション会場から厳選したお車をお届けします。

新車・中古車共に購入後のアフターフォローもおまかせください。

【買取】日頃、メンテナンスしている弊社だからこそ高く買い取ります。

記載項目
2面目に記載有と無パターンお願いします。
(有)桐ヶ丘自動車/04-5819-2746/ロゴ(添付ファイル)/HPアドレス:http://www.kirigaoka-jd.net/(桐ヶ丘自動車で検索窓でも可)
サイズ
A4
ページ数
両面
希望イメージ
シンプル 複雑
単色 カラフル
暗い 明るい
日常 高級
遊び心 厳粛
未来的 伝統的
女性的 男性的
希望する色
赤系、青系、水色系、緑系、黄・オレンジ系
納品ファイル
補足説明
ロゴを添付します。
2面目は既存のお客様に対してチラシを見て弊社で車を買っていただくというよりも、弊社でも車の販売をやっていることを知っていただいて、その時は相談してみようかなと思っていただくことが目的です。

例としてですが、上部に「買い替えを検討されている方」「桐ヶ丘自動車は販売もやっています」と入れていただくと良いかと思います。

買取の部分は必要がないかと思ってきました。
新車販売と中古車販売の2部構成でお願いします。

新車販売はまず「国産全メーカー全車種取り扱いできます」で
その新車販売の枠の中に「車の新しい乗り方」でリースのことを入れたいです。
リースが皆様全員にお得だとあてはまる訳ではないので
通常の新車販売もおまかせください的なことを表したいです。

リースの部分は伝えたいことのイメージ添付します。
『車両代』『車検』『自動車税』『メンテナンス代』「車を維持してくには大きな出費が発生」 → 毎月コミコミ定額
ご提案いただいた方々みなさま素晴らしいご提案ありがとうございます。
選定確約させていただきます。
修正をお願いしたいご提案があり修正後ので当選を決めさせていただきたく
締め切りを延長させていただきます。
今回のチラシは既存のお客様向けへのものです。
文章で伝えたい事を全部このチラシで伝えるよりも、単語やイラスト、図などで興味を持っていただき弊社のホームページを見ていただいたり、問い合わせをいただく流れができたらと思います。
カーリース「モクレンプラン」のイラストを添付追加します。
よかったら使ってください。
依頼金額を29700円に変更して、延長しました。
度々の延長申し訳ございません
提案していただいた皆様それぞれお気に入りな点があり
修正をお願いして当選を決めさせてください。
修正を個別にお願いをしますので、度々で申し訳ないのですが
よろしかったら修正をお願いします。
一番選考で重視している点は文字の大きさ、読みやすさです。
よろしくお願いします。
■ 選んだ理由

色使い、デザインが好みでした。
また修正の依頼をさせていただいた時も、こちらの考えを理解して提案していただきました。今後のお仕事も是非お願いしたいと思える方でした。

■ 提案者全員のお礼・コメント

今思うと、最初の依頼をした時点では漠然としたイメージしかなくご迷惑をお掛けしてしまったと思っております。沢山のご提案をいただき修正依頼をさせていただく中で、考えがまとまってきたと思います。何度も修正依頼をしてしまい申し訳ございませんでした。皆さんすばらしいご提案でした。ありがとうございます。

```html
<!DOCTYPE html>
<html lang="ja">
<head>
<meta charset="utf-8">
<title>桐ヶ丘自動車 車検のご案内</title>
<link href="https://fonts.googleapis.com/css2?family=Noto+Sans+JP:wght@400;500;700;900&display=swap" rel="stylesheet">
<style>
  :root{
    --blue:#1f63b8;
    --blue-light:#4a98e4;
    --navy:#17346f;
    --red:#e02a1d;
    --orange:#f29a18;
    --cream:#fff6cf;
    --green:#3d9a3a;
    --ink:#222;
    --line:#c9d6e6;
  }
  *{margin:0;padding:0;box-sizing:border-box}
  html,body{width:852px;height:1200px;overflow:hidden;background:#fff}
  body{font-family:"Noto Sans JP",sans-serif;color:var(--ink)}
  .flyer{position:relative;width:852px;height:1200px;border:2px solid var(--line);overflow:hidden}
  .top-band{position:absolute;left:0;top:0;width:100%;height:150px;background:linear-gradient(180deg,var(--blue-light),var(--blue))}
  .slogan{position:absolute;top:26px;width:100%;text-align:center;color:#fff;font-weight:900;font-size:48px;letter-spacing:2px;white-space:nowrap}
  .hero{position:absolute;left:28px;top:100px;width:796px;height:300px;background:linear-gradient(160deg,#f4f7fb 0%,#dfe8f3 60%,#cbd8e8 100%)}
  .tab{position:absolute;left:40px;top:112px;background:var(--blue);color:#fff;font-weight:700;font-size:30px;padding:4px 22px;border-radius:6px;border:2px solid #fff}
  .headline{position:absolute;left:28px;top:412px;width:796px;text-align:center;color:var(--navy);font-weight:900;font-size:37px;letter-spacing:1px;border-bottom:3px solid var(--blue);padding-bottom:6px;white-space:nowrap}
  .intro{position:absolute;left:56px;top:478px;width:750px;font-size:17px;line-height:1.6;font-weight:500}
  .intro p{text-indent:1em}
  .intro ol{list-style:none;margin-top:2px}
  .discount{position:absolute;left:28px;top:696px;width:396px}
  .discount-label{background:linear-gradient(90deg,var(--orange),#f5b433);color:#fff;font-weight:900;font-size:26px;padding:4px 18px;border-radius:6px 6px 0 0}
  .discount-table{background:var(--cream);border:2px solid var(--orange);border-top:none;padding:8px 18px}
  .row{display:flex;justify-content:space-between;align-items:baseline;padding:4px 0;border-bottom:1px dashed #e3c77a;white-space:nowrap}
  .row:last-child{border-bottom:none}
  .row .when{font-size:30px;font-weight:700}
  .row .amount{font-size:42px;font-weight:900;color:var(--red);line-height:1.3}
  .row .yen{font-size:28px}
  .note{margin-top:10px;font-size:14px;line-height:1.5}
  .assure{position:absolute;left:446px;top:696px;width:378px}
  .assure h2{font-size:24px;font-weight:900;line-height:1.45;color:var(--navy);white-space:nowrap}
  .checks{list-style:none;margin:12px 0;padding:10px 18px;border:2px solid var(--blue);border-radius:8px}
  .checks li{font-size:22px;font-weight:700;line-height:1.6;display:flex;align-items:center;gap:10px;white-space:nowrap}
  .checks svg{width:20px;height:20px;flex:none}
  .contact-lead{font-size:22px;font-weight:700;line-height:1.5;white-space:nowrap}
  .footer{position:absolute;left:28px;top:1090px;width:796px;height:88px;border-top:3px solid var(--green);display:flex;align-items:center;justify-content:space-between;padding:0 8px;white-space:nowrap}
  .brand{display:flex;align-items:center;gap:12px}
  .brand-dot{width:40px;height:40px;border-radius:50%;background:var(--green);flex:none}
  .brand-name{font-size:34px;font-weight:900;color:var(--green)}
  .tel{color:var(--red);font-weight:900;font-size:42px}
  .tel small{font-size:26px;margin-right:4px}
</style>
</head>
<body>
<div class="flyer">
  <div class="top-band"></div>
  <div class="slogan">安心・安全・快適なカーライフを。</div>
  <div class="hero" role="img" aria-label="クリップボードの上に置かれた赤いミニカー、電卓、レンチの写真"></div>
  <div class="tab">車検のご案内</div>

  <h1 class="headline">陸運局認証工場の安心安全快適まごころ車検</h1>

  <div class="intro">
    <p>当社は「ただ通すだけ」の激安車検ではなくお客様の目線でお得な車検プランをご提案します。安心・安全・快適にお乗り頂けるように「まごころ」を込めて整備します。</p>
    <p>また、使える部品は無理に交換は致しません！ご要望にあわせた車検を実施します。</p>
    <p>当社の車検の見積り説明時には</p>
    <ol>
      <li>1、交換しないと車検に合格しない部分</li>
      <li>2、安心のために交換しておいた方が良い部分</li>
      <li>3、快適に走行するために交換をオススメする部分</li>
    </ol>
  </div>

  <section class="discount">
    <div class="discount-label">早期予約割引</div>
    <div class="discount-table">
      <div class="row"><span class="when">3カ月以上前</span><span class="amount">3,000<span class="yen">円</span></span></div>
      <div class="row"><span class="when">2カ月前</span><span class="amount">2,000<span class="yen">円</span></span></div>
      <div class="row"><span class="when">1カ月前</span><span class="amount">1,000<span class="yen">円</span></span></div>
    </div>
    <p class="note">お早めのご予約をお待ちしております。<br>車検は満了日の1か月前から受けることができます。</p>
  </section>

  <section class="assure">
    <h2>桐ヶ丘車検なら、女性、<br>初めての方でも安心です。</h2>
    <ul class="checks">
      <li><svg viewBox="0 0 22 22"><circle cx="11" cy="11" r="9" fill="none" stroke="#1f63b8" stroke-width="2.5"/></svg>わかりやすい説明</li>
      <li><svg viewBox="0 0 22 22"><circle cx="11" cy="11" r="9" fill="none" stroke="#1f63b8" stroke-width="2.5"/></svg>納得できる料金</li>
      <li><svg viewBox="0 0 22 22"><circle cx="11" cy="11" r="9" fill="none" stroke="#1f63b8" stroke-width="2.5"/></svg>安心の技術力</li>
      <li><svg viewBox="0 0 22 22"><circle cx="11" cy="11" r="9" fill="none" stroke="#1f63b8" stroke-width="2.5"/></svg>選べる豊富な部品</li>
      <li><svg viewBox="0 0 22 22"><circle cx="11" cy="11" r="9" fill="none" stroke="#1f63b8" stroke-width="2.5"/></svg>作業完了後の清掃</li>
    </ul>
    <p class="contact-lead">メールまたは電話にて、<br>お気軽にご相談ください。</p>
  </section>

  <footer class="footer">
    <div class="brand">
      <span class="brand-dot"></span>
      <span class="brand-name">有限会社 桐ヶ丘自動車</span>
    </div>
    <div class="tel"><small>TEL</small>04-5819-2746</div>
  </footer>
</div>
</body>
</html>
```